Brave Otter Pet Sitting Postcard

I will be sending these postcards to homes in the neighborhood introducing my pet sitting business.

Include the following on the postcard:
Rosalind Hume
555-318-7294
www.braveotterpetsitting.example
help@braveotterpetsitting.example

```html
<!DOCTYPE html>
<html lang="en">
<head>
<meta charset="utf-8">
<title>Brave Otter Pet Sitting Postcard</title>
<link rel="stylesheet" href="https://fonts.googleapis.com/css2?family=Comfortaa:wght@400;600;700&display=swap">
<style>
  :root {
    --slate: #4a6877;
    --slate-dark: #3f5c6a;
    --yellow: #f6c516;
    --ring: #dfe8ea;
    --paper: #ffffff;
    --backdrop: #e8e8e8;
    --ink-soft: #4f6f7d;
  }
  * { box-sizing: border-box; margin: 0; padding: 0; }
  html, body { width: 1200px; height: 1177px; overflow: hidden; background: var(--backdrop); }
  body { position: relative; font-family: "Comfortaa", sans-serif; }

  .postcard {
    position: absolute; left: 195px; width: 810px; height: 540px;
    background: var(--paper); overflow: hidden;
    box-shadow: 0 6px 18px rgba(0,0,0,.18);
  }
  .postcard--front { top: 36px; }
  .postcard--back { top: 601px; }
  .postcard__art { position: absolute; inset: 0; width: 810px; height: 540px; }

  .abs { position: absolute; }

  .front__intro { left: 30px; top: 30px; width: 330px; color: #fff; font-size: 17px; line-height: 1.35; font-weight: 600; }
  .brand { display: flex; align-items: center; gap: 10px; color: var(--slate); font-weight: 700; font-size: 20px; }
  .brand__dot { width: 34px; height: 34px; border-radius: 50%; background: var(--yellow); flex: none; }
  .front__brand { left: 500px; top: 110px; }
  .front__tagline { left: 450px; top: 228px; width: 340px; text-align: center; color: var(--ink-soft); font-size: 15px; line-height: 1.4; font-weight: 600; }

  .contact-name { color: var(--yellow); font-weight: 700; font-size: 24px; line-height: 1.1; }
  .contact-phone { color: #fff; font-weight: 600; font-size: 30px; line-height: 1.15; }
  .front__contact { left: 92px; top: 456px; }
  .back__contact { left: 92px; top: 461px; }

  .web-list { left: 408px; top: 440px; color: var(--slate-dark); font-size: 17px; font-weight: 600; line-height: 1.7; }
  .web-list li { list-style: none; display: flex; align-items: center; gap: 9px; }
  .web-list svg { width: 15px; height: 15px; flex: none; }

  .services__tab { left: 0; top: 18px; width: 262px; height: 44px; background: var(--yellow); border-radius: 0 22px 22px 0; color: var(--slate); font-size: 24px; font-weight: 700; letter-spacing: 6px; padding: 8px 0 0 32px; }
  .services__list { left: 30px; top: 74px; color: #fff; font-size: 15.5px; line-height: 1.3; font-weight: 600; }
  .services__list li { list-style: none; }
  .back__brand { left: 420px; top: 60px; }
</style>
</head>
<body>

<section class="postcard postcard--front" aria-label="Postcard front">
  <svg class="postcard__art" viewBox="0 0 810 540" aria-hidden="false">
    <path d="M440 400 C560 370 700 380 810 405 V540 H360 Z" fill="var(--yellow)"/>
    <path d="M0 0 H330 C470 110 480 410 360 540 H0 Z" fill="var(--slate)"/>
    <circle cx="215" cy="285" r="148" fill="var(--ring)"/>
    <circle cx="215" cy="285" r="138" fill="#ffffff"/>
    <circle cx="215" cy="285" r="132" fill="#e9d4a8" role="img" aria-label="Photo of a puppy resting on a person's shoulder"/>
    <circle cx="545" cy="345" r="68" fill="var(--slate)"/>
    <circle cx="545" cy="345" r="60" fill="#6f9a58" role="img" aria-label="Photo of a black and white dog holding a red leash"/>
    <circle cx="700" cy="335" r="68" fill="var(--slate)"/>
    <circle cx="700" cy="335" r="60" fill="#e7a7c8" role="img" aria-label="Photo of a cat wearing a pink bonnet"/>
    <circle cx="52" cy="486" r="27" fill="var(--yellow)"/>
    <path d="M43 474 c2-2 5-2 6 1 l3 6 c1 2 0 4-2 5 l-2 1 c2 5 6 9 11 11 l1-2 c1-2 3-3 5-2 l6 3 c3 1 3 4 1 6 l-3 3 c-4 3-14 0-21-7 s-10-17-7-21 z" fill="var(--slate)"/>
  </svg>

  <p class="abs front__intro">Do you worry about your pets while you are gone from home? Let us take that worry away!</p>

  <div class="abs brand front__brand"><span class="brand__dot"></span>Brave Otter Pet Sitting</div>

  <p class="abs front__tagline">Whatever your pet needs - feeding, dog walking, TLC, playtime, etc.</p>

  <div class="abs front__contact">
    <p class="contact-name">Rosalind Hume</p>
    <p class="contact-phone">555-318-7294</p>
  </div>

  <ul class="abs web-list">
    <li><svg viewBox="0 0 16 16"><rect x="1.5" y="3.5" width="13" height="9" fill="none" stroke="currentColor" stroke-width="1.4"/><path d="M1.5 4 L8 9 L14.5 4" fill="none" stroke="currentColor" stroke-width="1.4"/></svg>help@braveotterpetsitting.example</li>
    <li><svg viewBox="0 0 16 16"><circle cx="8" cy="8" r="6.5" fill="none" stroke="currentColor" stroke-width="1.4"/><ellipse cx="8" cy="8" rx="3" ry="6.5" fill="none" stroke="currentColor" stroke-width="1.2"/><path d="M1.5 8 H14.5" stroke="currentColor" stroke-width="1.2"/></svg>www.braveotterpetsitting.example</li>
  </ul>
</section>

<section class="postcard postcard--back" aria-label="Postcard back">
  <svg class="postcard__art" viewBox="0 0 810 540">
    <defs>
      <clipPath id="back-panel"><path d="M0 0 H290 C420 120 450 400 330 540 H0 Z"/></clipPath>
    </defs>
    <g clip-path="url(#back-panel)">
      <rect width="810" height="540" fill="var(--slate)"/>
      <rect x="0" y="150" width="450" height="285" fill="#b9a27a" role="img" aria-label="Photo of a cat and a golden retriever sitting at a dining table by a window"/>
    </g>
    <circle cx="52" cy="491" r="27" fill="var(--yellow)"/>
    <path d="M43 479 c2-2 5-2 6 1 l3 6 c1 2 0 4-2 5 l-2 1 c2 5 6 9 11 11 l1-2 c1-2 3-3 5-2 l6 3 c3 1 3 4 1 6 l-3 3 c-4 3-14 0-21-7 s-10-17-7-21 z" fill="var(--slate)"/>
  </svg>

  <div class="abs services__tab">SERVICES</div>
  <ul class="abs services__list">
    <li>• Pet Sitting • Overnight</li>
    <li>• Pet Taxi • Pooper Scooper</li>
    <li>• Concierge Services</li>
    <li>• Holiday Schedule</li>
  </ul>

  <div class="abs brand back__brand"><span class="brand__dot"></span>Brave Otter Pet Sitting</div>

  <div class="abs back__contact">
    <p class="contact-name">Rosalind Hume</p>
    <p class="contact-phone">555-318-7294</p>
  </div>
</section>

</body>
</html>
```